Birch & Ember Website Design (Rustic/Western)

OVERVIEW
Birch & Ember Supply House (aka Birch & Ember) manufactures rustic / western furniture and décor for cabins, lodges, and ranches. We also offer a line of accessories to complement our product line.
WEB PAGE (www.BirchAndEmber.example)
We are looking for a new web page design to represent our mountain-style (log furniture) and country-style (barnwood furniture) product line. We would like to re-create our existing homepage with a similar style template for our product line.
Our website is currently under construction – a draft has been published as an example outline. We are currently using Plinkora.example for our online store.
THEME
The overall theme needs to appear rustic, yet elegant. Listed below are only suggestions, not requirements. Please use your own creativity.
* Photographs: We will use our own photographs, for now any photograph will suffice.
* Background Colors: dark brown (rgb 21-9-2), medium brown (rgb 39-17-4), light brown (rgb 72-34-3). White background is also an option.
* Font Colors: beige (rgb 233-164-118), gold (rgb 151-98-2)
• Mountain-Style Images: cabin, wildlife, mountains, fishing, wildlife, trees, etc.
* Mountain-Style Colors: hunter green
* Country-Style Images: western, ranch, barn, farm animals, horse buggies, horseshoes, etc.
* Country-Style Colors: maroon
Thanks to all who are participating.
Target Market(s)
Outdoor enthusiasts who enjoy mountain living or country living. Our primary target market is our local market and within a 100 mile radius of our location.
Industry/Entity Type
Construction
Requirements
Must have
- Rustic, yet elegant design.
Homepage and product template page for displaying each item.
Nice to have
- Source code and functionality is optional.
Mountain-Style theme to represent our collection of log furniture and décor suited for cabins and lodges. Suggested color: hunter green. Images may include cabin, wildlife, mountains, fishing, wildlife, trees, etc.
Country-Style theme to represent our collection of barnwood furniture and décor suited for farms and ranches. Suggested color: maroon. Images may include western, ranch, barn, farm animals, horse buggies, horseshoes, etc.

```html
<!DOCTYPE html>
<html lang="en">
<head>
<meta charset="utf-8">
<title>Birch &amp; Ember Supply House</title>
<link href="https://fonts.googleapis.com/css2?family=Roboto:wght@300;400;500;700&display=swap" rel="stylesheet">
<style>
:root{
  --dark:#150902;
  --medium:#271104;
  --light:#482203;
  --wood-a:#4a220a;
  --wood-b:#2a1206;
  --wood-c:#5a2c0e;
  --seam:#140701;
  --beige:#e9a476;
  --gold:#976202;
  --gold-bright:#c98a2c;
  --cream:#e8d6bd;
  --white:#ffffff;
  --btn:#2a1406;
  --btn-line:#8a5a1c;
}
*{box-sizing:border-box;margin:0;padding:0}
html,body{width:1200px;height:3203px;overflow:hidden}
body{position:relative;background:var(--dark);font-family:'Roboto',Arial,sans-serif;color:var(--beige)}
.abs{position:absolute}

/* wood planks: horizontal boards with dark seams */
.wood{
  background:
    repeating-linear-gradient(180deg,transparent 0 118px,var(--seam) 118px 121px),
    radial-gradient(ellipse 40% 12% at 20% 30%,rgba(110,50,15,.55),transparent 70%),
    radial-gradient(ellipse 35% 10% at 75% 62%,rgba(100,45,12,.5),transparent 70%),
    radial-gradient(ellipse 30% 8% at 55% 88%,rgba(20,8,2,.5),transparent 70%),
    linear-gradient(180deg,var(--wood-a) 0%,var(--wood-b) 18%,var(--wood-c) 34%,var(--wood-b) 52%,var(--wood-a) 70%,var(--wood-b) 86%,var(--wood-c) 100%);
}

/* header */
.topbar{left:0;top:0;width:1200px;height:50px;background:var(--medium)}
.topbar .login{left:843px;top:15px;font-size:15px;color:var(--cream)}
.topbar .search{left:904px;top:15px;width:138px;height:22px;background:#5a4a3c;border:1px solid #7a6a58;font-size:12px;color:#bfb3a4;padding:3px 6px}
.topbar .search svg{position:absolute;right:5px;top:4px}
.topbar .cart{left:1054px;top:15px;font-size:15px;color:var(--cream);display:flex;gap:6px;align-items:center}
.navband{left:0;top:50px;width:1200px;height:113px;background:
  radial-gradient(ellipse 30% 40% at 35% 100%,rgba(170,180,175,.7),transparent 70%),
  radial-gradient(ellipse 25% 35% at 80% 95%,rgba(160,170,170,.6),transparent 70%),
  linear-gradient(180deg,#e9ecef 0%,#f4f4f2 55%,#d3d8d4 100%)}
.nav{right:45px;top:115px;display:flex;gap:34px;font-size:16px;color:var(--gold);text-transform:uppercase;letter-spacing:.3px}
.logo{left:49px;top:0;width:242px;height:163px;background:#000;display:flex;flex-direction:column;align-items:center;justify-content:center;gap:8px}
.logo .mark{width:16px;height:16px;background:var(--gold-bright)}
.logo .name{font-size:22px;font-weight:700;color:var(--white);text-align:center;line-height:1.2}

.hero{left:0;top:163px;width:1200px;height:577px;background:
  radial-gradient(ellipse 18% 22% at 28% 80%,rgba(70,35,15,.85),transparent 72%),
  radial-gradient(ellipse 18% 22% at 70% 80%,rgba(80,40,18,.85),transparent 72%),
  radial-gradient(ellipse 22% 9% at 68% 45%,rgba(120,130,140,.85),transparent 75%),
  radial-gradient(ellipse 18% 8% at 90% 62%,rgba(110,120,130,.75),transparent 75%),
  radial-gradient(ellipse 30% 30% at 85% 25%,rgba(25,55,25,.9),transparent 70%),
  radial-gradient(ellipse 25% 25% at 40% 18%,rgba(40,75,30,.8),transparent 70%),
  linear-gradient(180deg,#c9d6d4 0%,#7fa06a 8%,#3d6a2a 22%,#6e9a34 40%,#8fb03e 60%,#6c8e2e 80%,#4f6a22 100%)}

/* gallery */
.gallery{left:0;top:740px;width:1200px;height:898px}
.tile{position:absolute;box-shadow:0 3px 8px rgba(0,0,0,.65)}
.btn{position:absolute;border:1px solid var(--btn-line);background:var(--btn);color:var(--beige);font-size:15px;text-transform:uppercase;display:flex;align-items:center;justify-content:center;letter-spacing:.5px}

/* lake banner */
.lake{left:0;top:1638px;width:1200px;height:493px;background:
  linear-gradient(180deg,rgba(0,0,0,0) 0%,rgba(0,0,0,.15) 100%),
  radial-gradient(ellipse 45% 18% at 78% 20%,rgba(30,60,25,.95),transparent 70%),
  radial-gradient(ellipse 30% 14% at 12% 30%,rgba(50,80,35,.9),transparent 70%),
  radial-gradient(ellipse 45% 14% at 78% 68%,rgba(25,45,25,.8),transparent 70%),
  radial-gradient(ellipse 30% 12% at 15% 70%,rgba(40,60,30,.75),transparent 70%),
  linear-gradient(180deg,#8fb0d2 0%,#c4d2dc 10%,#5c7e44 20%,#2f5226 34%,#3a5a2e 46%,#7f96a4 52%,#587684 64%,#3f5a5e 80%,#2c4428 100%)}
.lake h1{position:absolute;left:0;width:1200px;top:156px;text-align:center;font-weight:300;font-size:44px;color:var(--white);text-shadow:0 1px 4px rgba(0,0,0,.4)}
.lake .btn{left:478px;top:306px;width:246px;height:64px;font-size:18px;background:#3a1606;border-color:#3a1606}

/* info */
.info{left:0;top:2131px;width:1200px;height:419px}
.heading{position:absolute;display:flex;align-items:center;gap:14px;font-size:15px;font-weight:500;color:var(--cream);text-transform:uppercase;letter-spacing:.4px;white-space:nowrap}
.heading::before,.heading::after{content:"";flex:1;height:1px;background:var(--gold-bright)}
.para{position:absolute;font-size:16px;line-height:22px;color:var(--beige)}
.store-photo{left:505px;top:62px;width:187px;height:123px;border:3px solid var(--gold-bright);background:
  radial-gradient(ellipse 30% 40% at 30% 60%,rgba(160,120,80,.9),transparent 70%),
  radial-gradient(ellipse 30% 40% at 75% 45%,rgba(90,110,140,.8),transparent 70%),
  linear-gradient(180deg,#8a6a4a,#4a3424 55%,#6a4a2a)}
.store-name{left:436px;width:328px;top:198px;text-align:center;font-size:15px;font-weight:700;color:var(--cream)}
.store-addr{left:436px;width:328px;top:240px;text-align:center;font-size:14px;line-height:20px;color:var(--cream);text-transform:uppercase}

/* social */
.social{left:0;top:2550px;width:1200px;height:456px}
.social-band{left:0;top:0;width:1200px;height:56px;background:rgba(10,4,1,.55)}
.widget{position:absolute;background:var(--white);border:3px solid #e6d18a;color:#333;font-size:12px}
.fb-head{margin:6px;padding:5px 8px;background:#eceff5;border-bottom:1px solid #ccd;font-weight:700;font-size:13px}
.fb-page{display:flex;gap:8px;margin:8px 12px;align-items:flex-start}
.fb-page .sq{width:40px;height:40px;background:#5b74a8}
.fb-page b{color:#3b5998;font-size:14px}
.fb-like{margin-top:5px;display:inline-block;border:1px solid #bbb;background:#f2f2f2;padding:1px 6px;font-size:11px}
.fb-count{margin:4px 12px;font-size:11px}
.avatars{margin:6px 12px;height:150px;background:
  repeating-linear-gradient(90deg,transparent 0 48px,#fff 48px 52px),
  repeating-linear-gradient(180deg,transparent 0 58px,#fff 58px 75px),
  linear-gradient(135deg,#9a8f86,#5c5650 50%,#a59a8e)}
.fb-foot{margin:6px 12px;font-size:11px;color:#555;border-top:1px solid #ddd;padding-top:4px}
.tw-head{display:flex;gap:8px;align-items:center;padding:6px 8px}
.tw-head .sq{width:38px;height:38px;background:#4aa3df}
.tw-head b{color:#2a6fa8;font-size:14px;font-weight:500}
.tw-head small{display:block;font-size:10px;color:#666}
.tw-grid{margin:0 8px;height:116px;background:
  repeating-linear-gradient(90deg,transparent 0 36px,#fff 36px 40px),
  repeating-linear-gradient(180deg,transparent 0 52px,#fff 52px 58px),
  linear-gradient(135deg,#8c8279,#4f4a46 45%,#b3a89b)}
.field{position:absolute;left:813px;width:333px;border:1px solid var(--btn-line);background:rgba(0,0,0,.15);font-size:15px;color:var(--cream);padding:6px 8px}

/* footer */
.footer{left:0;top:3006px;width:1200px;height:197px;background:var(--dark)}
.footer .pay{left:128px;top:55px;font-size:17px;font-weight:700;color:var(--cream)}
.cards{left:74px;top:81px;display:flex;gap:5px}
.cards span{width:40px;height:26px;background:#d9d2c6;border-radius:2px}
.copy{left:74px;top:135px;font-size:13px;line-height:18px;color:var(--cream)}
.contact-title{left:430px;width:340px;top:12px;text-align:center;font-size:17px;font-weight:500;color:var(--cream);text-transform:uppercase}
.contact-lines{left:380px;width:440px;top:56px;text-align:center;font-size:14px;line-height:20px;color:var(--beige);text-transform:uppercase}
.contact-row{left:380px;width:440px;text-align:center;font-size:14px;color:var(--cream);display:flex;justify-content:center;gap:6px;align-items:center}
.follow-title{left:880px;width:200px;top:12px;text-align:center;font-size:17px;font-weight:500;color:var(--cream);text-transform:uppercase}
.follow-icons{left:906px;top:62px;display:flex;gap:16px}
.follow-icons span{width:18px;height:18px;border-radius:50%;background:var(--beige)}
</style>
</head>
<body>

<header>
  <div class="abs topbar">
    <span class="abs login">Login</span>
    <div class="abs search">Search
      <svg width="12" height="12" viewBox="0 0 12 12"><circle cx="5" cy="5" r="3.5" fill="none" stroke="#ddd" stroke-width="1.5"/><line x1="7.5" y1="7.5" x2="11" y2="11" stroke="#ddd" stroke-width="1.5"/></svg>
    </div>
    <span class="abs cart">
      <svg width="16" height="14" viewBox="0 0 16 14"><path d="M1 1h3l2 8h8l1.5-6H5" fill="none" stroke="#e0a32a" stroke-width="1.6"/><circle cx="7" cy="12" r="1.3" fill="#e0a32a"/><circle cx="13" cy="12" r="1.3" fill="#e0a32a"/></svg>
      Cart(0)</span>
  </div>
  <div class="abs navband" role="img" aria-label="Soft misty mountain skyline behind the navigation"></div>
  <nav class="abs nav">
    <span>Company</span><span>Bargains</span><span>Furniture</span><span>Wall Decor</span><span>Lighting</span><span>Accessories</span>
  </nav>
  <div class="abs logo">
    <span class="mark"></span>
    <span class="name">Birch &amp; Ember<br>Supply House</span>
  </div>
</header>

<section class="abs hero" role="img" aria-label="Two riders on horseback overlooking a creek winding through a green mountain valley with pine trees"></section>

<section class="abs gallery wood">
  <div class="tile" style="left:44px;top:61px;width:257px;height:259px;background:radial-gradient(ellipse 45% 15% at 50% 62%,rgba(150,80,30,.9),transparent 75%),linear-gradient(180deg,#7fa8d4 0%,#a9c2d8 30%,#9aa866 42%,#7c9a3c 70%,#5f7e2c 100%)" role="img" aria-label="Log benches on a grassy prairie"></div>
  <div class="tile" style="left:44px;top:347px;width:257px;height:226px;background:radial-gradient(ellipse 35% 30% at 30% 65%,rgba(220,130,30,.95),transparent 70%),radial-gradient(ellipse 35% 30% at 75% 60%,rgba(200,150,40,.9),transparent 70%),linear-gradient(180deg,#a9b8c8 0%,#8a8e9a 25%,#b86e22 55%,#6d6a2c 85%,#4a5a28 100%)" role="img" aria-label="Autumn aspens below jagged mountain peaks"></div>
  <div class="tile" style="left:44px;top:603px;width:257px;height:237px;background:radial-gradient(ellipse 40% 25% at 50% 55%,rgba(60,40,30,.8),transparent 70%),linear-gradient(180deg,#8a3a22 0%,#7a3420 40%,#b07a48 70%,#d4aa78 100%)" role="img" aria-label="Rustic table lamps on a wooden shelf against brick"></div>

  <div class="tile" style="left:330px;top:61px;width:256px;height:172px;background:radial-gradient(ellipse 18% 25% at 30% 28%,#f2c080,transparent 80%),radial-gradient(ellipse 18% 25% at 70% 28%,#f2c080,transparent 80%),linear-gradient(180deg,#b0603a,#8a4020 55%,#5a2a12)" role="img" aria-label="Pair of log lamps with glowing shades"></div>
  <div class="tile" style="left:330px;top:260px;width:256px;height:163px;background:radial-gradient(ellipse 42% 38% at 50% 48%,rgba(170,110,55,.95),transparent 75%),linear-gradient(180deg,#e4dccc,#c9a070 50%,#8a5a2a)" role="img" aria-label="Barnwood dresser with drawers"></div>
  <div class="tile" style="left:330px;top:453px;width:256px;height:167px;background:radial-gradient(ellipse 40% 22% at 50% 42%,rgba(210,170,110,.95),transparent 75%),linear-gradient(180deg,#bdb59a,#9aa072 45%,#6a7a3a 100%)" role="img" aria-label="Log bench standing on grass"></div>

  <div class="tile" style="left:611px;top:61px;width:259px;height:172px;background:radial-gradient(ellipse 40% 35% at 45% 60%,rgba(170,90,40,.95),transparent 75%),linear-gradient(180deg,#eeeae2,#c9b8a4 40%,#7a4a2a 100%)" role="img" aria-label="Log dining table with chairs"></div>
  <div class="tile" style="left:611px;top:260px;width:259px;height:188px;background:radial-gradient(ellipse 18% 14% at 20% 45%,rgba(200,30,30,.9),transparent 75%),radial-gradient(ellipse 30% 35% at 70% 60%,rgba(200,160,90,.9),transparent 75%),linear-gradient(180deg,#6a625a,#8a7a64 45%,#5a5040)" role="img" aria-label="Wagon wheel and wooden planters with red flowers"></div>
  <div class="tile" style="left:611px;top:485px;width:259px;height:202px;background:radial-gradient(ellipse 45% 30% at 50% 50%,rgba(110,50,25,.9),transparent 75%),linear-gradient(180deg,#a86a3a,#c07a3a 45%,#7a3a1a)" role="img" aria-label="Painting of horses running"></div>

  <div class="tile" style="left:897px;top:61px;width:259px;height:192px;background:radial-gradient(ellipse 40% 25% at 50% 45%,rgba(200,190,175,.7),transparent 75%),linear-gradient(180deg,#3a3028,#5a4a3a 50%,#2a2018)" role="img" aria-label="Weathered barnwood candle holders"></div>
  <div class="tile" style="left:897px;top:283px;width:259px;height:253px;background:radial-gradient(ellipse 45% 35% at 50% 45%,rgba(215,170,100,.95),transparent 75%),linear-gradient(180deg,#8a9aa8,#b08a5a 45%,#6a4a2a)" role="img" aria-label="Row of log bar stools"></div>
  <div class="tile" style="left:897px;top:563px;width:259px;height:277px;background:radial-gradient(ellipse 22% 25% at 62% 75%,rgba(140,70,25,.95),transparent 75%),linear-gradient(180deg,#7aa6d6 0%,#b0c8dc 15%,#8fa858 35%,#7a9a3c 65%,#5f7e2c 100%)" role="img" aria-label="Barrel table and horse buggy in a meadow"></div>

  <span class="btn" style="left:517px;top:805px;width:166px;height:44px">Show More</span>
</section>

<section class="abs lake" role="img" aria-label="Mountain lake reflecting forested hills">
  <h1>Nam libero tempore cum soluta nobis</h1>
  <span class="btn">Download Brochure</span>
</section>

<section class="abs info wood">
  <h2 class="heading" style="left:49px;width:335px;top:24px">About Us</h2>
  <p class="para" style="left:49px;top:70px;width:335px;text-align:justify">Birch &amp; Ember was established in 2000 as a part-time picture framing business and offered fine-art photography by attending local arts &amp; crafts events. In 2011 we expanded our product line by adding antiques and western décor. In 2012 we began building rustic &amp; western furniture and accessories.</p>
  <span class="btn" style="left:153px;top:308px;width:130px;height:32px">More</span>

  <h2 class="heading" style="left:436px;width:328px;top:24px">Our Antiques &amp; Collectibles</h2>
  <div class="abs store-photo" role="img" aria-label="Interior of the antique market"></div>
  <div class="abs store-name">PINECREST</div>
  <div class="abs store-addr">Antique Market<br>C/O Birch &amp; Ember Supply House<br>412 Cedar Ridge Road Pinecrest, MT 59000</div>
  <span class="btn" style="left:540px;top:308px;width:128px;height:32px">Direction</span>

  <h2 class="heading" style="left:788px;width:365px;top:24px">Nostrum Exercitationem</h2>
  <p class="para" style="left:808px;top:86px;width:340px">Itaque earum rerum hic tenetur a sapiente delectus, ut aut reiciendis voluptatibus alias consequatur aut perferendis doloribus asperiores repellat.</p>
  <span class="btn" style="left:941px;top:308px;width:131px;height:32px">More</span>
</section>

<section class="abs social wood">
  <div class="abs social-band"></div>
  <h2 class="heading" style="left:49px;width:335px;top:18px">Find Us on Facelog</h2>
  <div class="widget" style="left:54px;top:96px;width:330px;height:330px">
    <div class="fb-head">Find us on Facelog</div>
    <div class="fb-page"><span class="sq"></span><div><b>Facelog Pages</b><br><span class="fb-like">Like</span></div></div>
    <div class="fb-count">1,988,819 people like <b>Facelog Pages</b>.</div>
    <div class="avatars" role="img" aria-label="Grid of follower profile pictures"></div>
    <div class="fb-foot">Facelog social plugin</div>
  </div>

  <h2 class="heading" style="left:429px;width:342px;top:18px">Follow Us on Chirpline</h2>
  <div class="widget" style="left:429px;top:96px;width:342px;height:197px">
    <div class="tw-head"><span class="sq"></span><div><b>Follow us on Chirpline</b><small>Follow @birchember 1,208 followers</small></div></div>
    <div class="tw-grid" role="img" aria-label="Grid of follower profile pictures"></div>
  </div>

  <h2 class="heading" style="left:813px;width:340px;top:18px">Quick Contact</h2>
  <div class="field" style="top:99px;height:34px">Name</div>
  <div class="field" style="top:145px;height:34px">E-mail</div>
  <div class="field" style="top:192px;height:124px">Message</div>
  <span class="btn" style="left:1025px;top:333px;width:121px;height:32px">Submit</span>
</section>

<footer class="abs footer wood">
  <span class="abs pay">Paywell</span>
  <div class="abs cards" role="img" aria-label="Accepted payment cards"><span></span><span></span><span></span><span></span></div>
  <p class="abs copy">© 2014 Copyright Birch &amp; Ember Supply House<br>All Rights Reserved.</p>

  <h3 class="abs contact-title">Contact Us</h3>
  <p class="abs contact-lines">Birch &amp; Ember Supply House<br>Elk Hollow, MT 59001</p>
  <div class="abs contact-row" style="top:104px">
    <svg width="12" height="12" viewBox="0 0 12 12"><path d="M2 1l2 0 1 3-1.5 1a7 7 0 0 0 3.5 3.5L8 7l3 1v2a1 1 0 0 1-1 1A9 9 0 0 1 1 2a1 1 0 0 1 1-1z" fill="#e9a476"/></svg>
    (555) 014-2290</div>
  <div class="abs contact-row" style="top:130px">
    <svg width="13" height="10" viewBox="0 0 13 10"><rect x=".5" y=".5" width="12" height="9" fill="#e9a476"/><path d="M.5 .5l6 5 6-5" fill="none" stroke="#150902"/></svg>
    hello@birchandember.example</div>
  <div class="abs contact-row" style="top:152px">www.BirchAndEmber.example</div>

  <h3 class="abs follow-title">Follow Us</h3>
  <div class="abs follow-icons" role="img" aria-label="Social network links"><span></span><span></span><span></span><span></span><span></span></div>
</footer>

</body>
</html>
```